Quorandel Web design

I described what I need to the doc.
Please see the my request from the following URL.
http://fernhollow57.pebbly.jp/QuorandelHPdraft.pdf

Please see my request and don't suggest boring typical web.

We need the innovation and the unique suggestion from you.

The log updated the site. 

Please see and design on your mind.

Thanks
quorandel

The flag on countries are for changing language.
It must be small, all designs are big.

Seeing the logo image, the we must be cool with white/black/grey.
Most designs are colorful or for kids.

```html
<!DOCTYPE html>
<html lang="ja">
<head>
<meta charset="utf-8">
<title>Quorandel — Product Process</title>
<link href="https://fonts.googleapis.com/css2?family=Jost:wght@400;500;600&family=Noto+Sans+JP:wght@400;500&display=swap" rel="stylesheet">
<style>
  :root {
    --bg-light: #f1f1f1;
    --bg-dark: #d4d4d4;
    --ink: #4a4a4a;
    --ink-soft: #5e5e5e;
    --icon: #8c8c8c;
    --axis: #9a9a9a;
    --accent: #7a5198;
    --white: #ffffff;
    --brand-faint: #b9b9b9;
  }
  * { margin: 0; padding: 0; box-sizing: border-box; }
  html, body { width: 1200px; height: 750px; overflow: hidden; }
  body {
    position: relative;
    font-family: "Jost", sans-serif;
    background: radial-gradient(ellipse 70% 70% at 50% 40%, var(--bg-light), var(--bg-dark));
    color: var(--ink);
  }
  .stage { position: absolute; inset: 0; }
  .brand-faint {
    position: absolute; left: 496px; top: 388px;
    font-family: "Jost", sans-serif; font-weight: 600;
    font-size: 46px; letter-spacing: 2px; color: var(--brand-faint);
  }
  .axis-label {
    position: absolute; font-size: 14px; letter-spacing: .5px; color: var(--ink-soft);
  }
  .axis-label.value { left: 94px; top: 223px; }
  .axis-label.process { right: 126px; top: 609px; }
  .stage-label {
    position: absolute; text-align: center; font-size: 14.5px; line-height: 18px;
    letter-spacing: .4px; color: var(--ink-soft); transform: translateX(-50%);
  }
  .stage-label.active { color: var(--accent); }
  .callout {
    position: absolute; left: 418px; top: 224px; width: 400px; height: 190px;
    background: var(--accent); border-radius: 6px; color: var(--white);
    padding: 20px 24px 0 25px;
    box-shadow: 0 2px 6px rgba(0,0,0,.15);
  }
  .callout::after {
    content: ""; position: absolute; left: 54px; bottom: -26px;
    border-left: 0 solid transparent; border-right: 32px solid transparent;
    border-top: 26px solid var(--accent);
  }
  .callout-title { font-size: 19px; font-weight: 500; letter-spacing: .3px; margin-bottom: 14px; }
  .callout-body {
    font-family: "Noto Sans JP", sans-serif; font-size: 12.6px; line-height: 21px;
    white-space: pre-line;
  }
  .about {
    position: absolute; left: 534px; top: 688px;
    display: flex; align-items: center; gap: 12px;
  }
  .about-title { font-size: 27px; font-weight: 600; letter-spacing: -.5px; color: #555; }
  .about-square { width: 26px; height: 26px; background: #666; border-radius: 2px; }
</style>
</head>
<body>
<svg class="stage" width="1200" height="750" viewBox="0 0 1200 750">
  <defs>
    <linearGradient id="bowl" x1="0" y1="0" x2="0" y2="1">
      <stop offset="0" stop-color="#ffffff" stop-opacity="0"/>
      <stop offset=".45" stop-color="#fafafa" stop-opacity=".5"/>
      <stop offset=".8" stop-color="#e8e8e8"/>
      <stop offset="1" stop-color="#d2d2d2"/>
    </linearGradient>
    <linearGradient id="axisGrad" x1="0" y1="0" x2="1" y2="0">
      <stop offset="0" stop-color="#b5b5b5"/>
      <stop offset="1" stop-color="#8a8a8a"/>
    </linearGradient>
  </defs>
  <ellipse cx="622" cy="270" rx="470" ry="332" fill="url(#bowl)"/>
  <path d="M152 330 A470 332 0 0 0 1092 330" fill="none" stroke="#ffffff" stroke-width="3" opacity=".8"/>

  <!-- axes -->
  <rect x="111" y="268" width="6" height="367" fill="url(#axisGrad)"/>
  <polygon points="114,254 106,272 122,272" fill="#9a9a9a"/>
  <rect x="180" y="644" width="885" height="6" fill="#9c9c9c"/>
  <polygon points="1080,647 1062,639 1062,655" fill="#9a9a9a"/>

  <!-- stage markers -->
  <g fill="#ececec" stroke="#ffffff" stroke-width="2">
    <circle cx="165" cy="372" r="8"/>
    <circle cx="247" cy="484" r="8"/>
    <circle cx="624" cy="601" r="8"/>
    <circle cx="871" cy="553" r="8"/>
  </g>
  <circle cx="402" cy="567" r="7" fill="#ffffff"/>
  <circle cx="402" cy="567" r="4.5" fill="var(--accent)"/>

  <!-- bulb icon -->
  <g fill="var(--icon)">
    <circle cx="283" cy="388" r="13"/>
    <rect x="276" y="396" width="14" height="10"/>
    <rect x="277" y="407" width="12" height="3" rx="1"/>
    <rect x="278" y="411" width="10" height="3" rx="1"/>
  </g>
  <!-- people icon -->
  <g fill="var(--accent)">
    <circle cx="444" cy="467" r="7"/>
    <path d="M433 494 q1-16 11-17 q11 1 14 17z"/>
    <circle cx="428" cy="465" r="9"/>
    <path d="M412 494 q1-20 16-20 q15 0 17 20z"/>
  </g>
  <!-- image icon -->
  <g>
    <rect x="597" y="494" width="44" height="33" fill="none" stroke="var(--icon)" stroke-width="3"/>
    <polygon points="601,523 614,507 623,517 629,511 637,523" fill="var(--icon)"/>
    <circle cx="630" cy="503" r="3.5" fill="var(--icon)"/>
  </g>
  <!-- robot-style unit icon (no features) -->
  <g fill="var(--icon)">
    <rect x="841" y="433" width="3" height="10"/>
    <circle cx="842.5" cy="434" r="2.5"/>
    <rect x="825" y="443" width="35" height="35" rx="10"/>
  </g>
</svg>

<div class="brand-faint">QUORANDEL</div>

<div class="axis-label value">VALUE</div>
<div class="axis-label process">PRODUCT PROCESS</div>

<div class="stage-label" style="left:284px;top:422px">INNOVATIVE<br>PLANNING</div>
<div class="stage-label active" style="left:435px;top:502px">ODM/EMS<br>CONSULTING</div>
<div class="stage-label" style="left:621px;top:541px">OFFSHORE SOFTWARE<br>DESIGN SERVICES</div>
<div class="stage-label" style="left:843px;top:488px">AUTOMATED<br>VERIFICATION</div>

<div class="callout">
  <div class="callout-title">ODM/EMS CONSULTING</div>
  <p class="callout-body">企画/マーケティングを日本・横浜に、R&amp;D を中国・
大連におくグローバルソフトウェアカ ンパニーです
。 役員はノルヴェクソフト出身者により構成されてお
り、スマートフォンや電子機器の開発を 熟知したエ
ンジニアが在籍しております。</p>
</div>

<div class="about">
  <span class="about-title">ABOUT US</span>
  <span class="about-square"></span>
</div>
</body>
</html>
```